Nectarine Point of Sale Cards for Grocery Retail Markets

We are looking to update our Nectarine point of sale card and price card. The cards will need to be 7" x 11" with a .125 bleed - one sided. See attached for the old versions. We would like this to use photos that look like true Washington State Peaches. Here are the bullet points we would like to use: - New Crop!- Tree Ripened- Excellent FlavorNOTE: The price card just needs to have a space where a retailer can write in the sale price of the item. See attachment with the white box.

Target Market(s)

Retail market shoppers

Requirements
Must have
• Pictures of Nectarines Only

```html
<!DOCTYPE html>
<html lang="en">
<head>
<meta charset="utf-8">
<title>Nectarine Point of Sale Card</title>
<link rel="stylesheet" href="https://fonts.googleapis.com/css2?family=Kaushan+Script&family=Open+Sans:wght@300;700&display=swap">
<style>
  :root {
    --page-bg: #eceeec;
    --leaf-green: #3f9a38;
    --brand-green: #1f7a34;
    --white: #ffffff;
    --fruit-red: #e0503a;
    --silver-light: #f4f4f4;
    --silver-dark: #8c8c8c;
  }
  html, body {
    margin: 0;
    width: 1200px;
    height: 1200px;
    overflow: hidden;
    background: var(--page-bg);
  }
  .pos-card {
    position: absolute;
    left: 50px;
    top: 250px;
    width: 1100px;
    height: 700px;
    display: block;
  }
  .brand-name {
    font-family: "Open Sans", sans-serif;
    font-weight: 700;
    font-size: 27px;
    fill: var(--brand-green);
  }
  .headline {
    font-family: "Kaushan Script", cursive;
    font-size: 94px;
    fill: var(--white);
  }
  .subhead {
    font-family: "Open Sans", sans-serif;
    font-weight: 300;
    font-size: 34px;
    fill: var(--white);
  }
  .bullet-text {
    font-family: "Kaushan Script", cursive;
    font-size: 48px;
    fill: var(--white);
  }
  .bullet-dot { fill: var(--white); }
  .green-panel { fill: var(--leaf-green); }
  .soft-arc { fill: var(--white); opacity: 0.1; }
  .price-box { fill: var(--white); }
  .brand-bubble { fill: var(--white); opacity: 0.78; }
  .brand-dot { fill: var(--fruit-red); }
</style>
</head>
<body>
<svg class="pos-card" viewBox="0 0 1236 786" xmlns="http://www.w3.org/2000/svg">
  <defs>
    <radialGradient id="fruit-tones" cx="0.55" cy="0.55" r="0.75">
      <stop offset="0" stop-color="#f28a2c"/>
      <stop offset="0.35" stop-color="#f0a460"/>
      <stop offset="0.6" stop-color="#d96a4e"/>
      <stop offset="1" stop-color="#8a6a5e"/>
    </radialGradient>
    <linearGradient id="silver-edge" x1="0" x2="1" y1="0" y2="0">
      <stop offset="0" stop-color="var(--silver-dark)"/>
      <stop offset="0.5" stop-color="var(--silver-light)"/>
      <stop offset="1" stop-color="var(--silver-dark)"/>
    </linearGradient>
    <clipPath id="card-clip"><rect width="1236" height="786"/></clipPath>
  </defs>

  <g clip-path="url(#card-clip)">
    <g class="hero-photo" role="img" aria-label="Photo of whole and halved ripe nectarines with mint leaves on a wooden table">
      <rect width="1236" height="520" fill="url(#fruit-tones)"/>
    </g>

    <ellipse class="brand-bubble" cx="220" cy="85" rx="450" ry="140"/>
    <g class="brand">
      <circle class="brand-dot" cx="118" cy="97" r="42"/>
      <text class="brand-name" x="192" y="94">Cascade Orchard</text>
      <text class="brand-name" x="192" y="123">Growers Board</text>
    </g>

    <text class="headline" x="630" y="345" text-anchor="middle">Taste The Difference!</text>
    <text class="subhead" x="620" y="422" text-anchor="middle">Washington State Peaches</text>

    <path class="green-panel" d="M0 310 Q618 670 1236 310 L1236 786 L0 786 Z"/>
    <path d="M0 310 Q618 670 1236 310" fill="none" stroke="url(#silver-edge)" stroke-width="7"/>

    <circle class="soft-arc" cx="340" cy="1000" r="500"/>
    <circle class="soft-arc" cx="1010" cy="1020" r="480"/>

    <g class="bullets">
      <circle class="bullet-dot" cx="107" cy="556" r="18"/>
      <text class="bullet-text" x="172" y="570">New Crop!</text>
      <circle class="bullet-dot" cx="107" cy="636" r="18"/>
      <text class="bullet-text" x="172" y="650">Tree Ripened</text>
      <circle class="bullet-dot" cx="107" cy="716" r="18"/>
      <text class="bullet-text" x="172" y="730">Excellent Flavor</text>
    </g>

    <path class="price-box" d="M780 786 L780 572 Q780 527 825 527 L1191 527 Q1236 527 1236 572 L1236 786 Z"/>
  </g>
</svg>
</body>
</html>
```